Fitness Body Weight Exercises Book Cover

Need a book cover design for a new book

This book is going to market to people to get in shape by playing a fitness dice game call FlexRUMBA The dice game

When people see the cover they should see that this is a book that can help them get in shape. We are positioning the guru as an expert inside of the fitness niche

Target Market(s)

fitness

Requirements
Must have
• The name of the book which is

"The Grand Victor Floorwork Regimen"

Tagline -

The Worlds #1 Resource For Combat Strength Training Using Body Weight Exercises For Men, Women and Children

__________

Featuring FlexRUMBA The Dice Game (TM)

___________________________
ON THE BACK COVER

Image with Bren with his gold medal
with these words
No Weights, No Problem

_____-

front cover
the image with him doing a push up should be on the front of the cover with these words

_________
Nice to have
• Maybe

"Bren Presents ...."

The Grand Victor Floorwork Regimen

```html
<!DOCTYPE html>
<html lang="en">
<head>
<meta charset="utf-8">
<title>The Grand Victor Floorwork Regimen – Book Cover</title>
<link rel="stylesheet" href="https://fonts.googleapis.com/css2?family=Anton&family=Quicksand:wght@500;700&family=Montserrat:wght@500&display=swap">
<style>
  :root{
    --navy:#12162e;
    --yellow:#fbbf1c;
    --amber:#f6a81a;
    --gold:#f4b21f;
    --red:#c3161c;
    --ink:#111111;
    --white:#ffffff;
    --tagline:#1c1a16;
    --photo-gold:#9a7022;
  }
  *{margin:0;padding:0;box-sizing:border-box}
  html,body{width:1200px;height:831px;overflow:hidden;background:#fff}
  .cover{position:relative;width:1200px;height:831px;overflow:hidden}

  /* back cover */
  .back{position:absolute;left:0;top:0;width:556px;height:831px;background:var(--navy);overflow:hidden}
  .back-shapes{position:absolute;inset:0}
  .back-photo{position:absolute;left:68px;top:72px;width:450px;height:610px;
    border-radius:200px 200px 40px 40px;
    background:linear-gradient(180deg,#6b4a33 0%,#a3704b 40%,#8a5c3c 100%);opacity:.92}
  .slogan{position:absolute;left:40px;top:302px;transform-origin:0 0;transform:rotate(-90deg);
    font-family:"Anton",sans-serif;font-size:44px;line-height:50px;letter-spacing:.5px;white-space:nowrap;font-weight:400}
  .slogan .line-1{color:var(--white);display:block}
  .slogan .line-2{color:var(--yellow);display:block}
  .back-credits{position:absolute;left:45px;top:698px;font-family:"Quicksand",sans-serif;color:var(--ink)}
  .back-credits .feature{font-size:18px;font-weight:500;line-height:22px}
  .back-credits .meta{font-size:14.5px;font-weight:700;line-height:22px;margin-top:9px}
  .back-credits sup{font-size:10px}
  .barcode-box{position:absolute;left:345px;top:705px;width:167px;height:86px;background:var(--white)}

  /* spine */
  .spine{position:absolute;left:556px;top:0;width:90px;height:831px;background:#000}
  .spine-title{position:absolute;left:0;top:0;width:90px;height:831px}
  .spine-title text{font-family:"Anton",sans-serif}
  .spine-author{position:absolute;left:80px;top:255px;transform-origin:0 0;transform:rotate(90deg);
    font-family:"Montserrat",sans-serif;font-weight:500;font-size:19px;letter-spacing:13px;color:var(--white);white-space:nowrap}

  /* front cover */
  .front{position:absolute;left:646px;top:0;width:554px;height:831px;
    background:radial-gradient(ellipse at 60% 35%,#ffc632 0%,var(--gold) 55%,var(--amber) 100%);overflow:hidden}
  .front-photo{position:absolute;left:0;top:404px;width:554px;height:427px;
    border-radius:260px 120px 0 0;
    background:linear-gradient(180deg,#b58428 0%,var(--photo-gold) 45%,#7a5518 100%)}
  .presents-band{position:absolute;left:114px;top:38px;width:331px;height:30px;background:var(--red);
    font-family:"Montserrat",sans-serif;font-weight:500;font-size:21px;letter-spacing:10px;color:var(--white);
    line-height:30px;text-align:center;white-space:nowrap;padding-left:10px}
  .front-title{position:absolute;left:114px;top:72px;width:332px;height:290px}
  .front-title text{font-family:"Anton",sans-serif}
  .tagline{position:absolute;left:114px;top:366px;width:340px;font-family:"Quicksand",sans-serif;font-weight:700;
    font-size:18px;line-height:22px;color:var(--tagline);white-space:nowrap}
  .front-feature{position:absolute;left:280px;top:773px;width:320px;text-align:center;transform:translateX(-50%);
    font-family:"Quicksand",sans-serif;font-weight:700;font-size:17px;line-height:21px;color:var(--white)}
</style>
</head>
<body>
<div class="cover">

  <section class="back">
    <svg class="back-shapes" width="556" height="831" viewBox="0 0 556 831">
      <polygon points="230,0 556,0 556,190" fill="#f7b81e"/>
      <polygon points="330,0 556,0 556,120" fill="#fcc62a"/>
      <polygon points="0,380 556,720 556,831 0,831" fill="#f6b01c" opacity=".55"/>
      <polygon points="0,520 556,690 556,831 0,831" fill="#f8b91e"/>
      <path d="M0,660 Q200,620 330,650 T556,640 L556,831 L0,831 Z" fill="#fbc52c"/>
      <line x1="190" y1="0" x2="556" y2="210" stroke="#f7c01f" stroke-width="1.5"/>
      <line x1="0" y1="470" x2="150" y2="560" stroke="#fbc52c" stroke-width="6" stroke-linecap="round"/>
    </svg>
    <div class="back-photo" role="img" aria-label="Photo of Bren smiling, wearing a cap and his gold medal"></div>
    <h2 class="slogan"><span class="line-1">NO WEIGHTS,</span><span class="line-2">NO PROBLEM</span></h2>
    <div class="back-credits">
      <p class="feature">FEATURING<br>FlexRUMBA The Dice Game<sup>TM</sup></p>
      <p class="meta">Published By:<br>Date:</p>
    </div>
    <div class="barcode-box"></div>
  </section>

  <section class="spine">
    <svg class="spine-title" viewBox="0 0 90 831" aria-label="The Grand Victor Floorwork Regimen">
      <text transform="translate(15,55) rotate(90)" font-size="34" fill="var(--white)" textLength="722" lengthAdjust="spacingAndGlyphs">THE GRAND <tspan fill="var(--yellow)">VICTOR</tspan> FLOORWORK <tspan fill="var(--yellow)">REGIMEN</tspan></text>
    </svg>
    <p class="spine-author">BREN PRESENTS</p>
  </section>

  <section class="front">
    <div class="front-photo" role="img" aria-label="Photo of Bren doing a push-up, tinted gold"></div>
    <div class="presents-band">BREN PRESENTS</div>
    <svg class="front-title" viewBox="0 0 332 290" aria-label="The Grand Victor Floorwork Regimen">
      <text x="0" y="66" font-size="74" fill="var(--ink)" textLength="332" lengthAdjust="spacingAndGlyphs">THE GRAND</text>
      <text x="0" y="142" font-size="74" fill="var(--red)" textLength="332" lengthAdjust="spacingAndGlyphs">VICTOR</text>
      <text x="0" y="214" font-size="68" fill="var(--ink)" textLength="332" lengthAdjust="spacingAndGlyphs">FLOORWORK</text>
      <text x="0" y="286" font-size="72" fill="var(--red)" textLength="332" lengthAdjust="spacingAndGlyphs">REGIMEN</text>
    </svg>
    <p class="tagline">The Worlds #1 Resource For Combat<br>Strength Training Using<br>Body Weight Exercises<br>For Men, Women<br>and Children.</p>
    <p class="front-feature">FEATURING FLEXRUMBA<br>THE DICE GAME (TM)</p>
  </section>

</div>
</body>
</html>
```